Business card for a gourmet fruit and vegetable retail store

Please design a business card for our boutique gourmet fruit and vegetable food store using attached logo design, with the colour options of white, black and lime green. We would like it to be unique and classic, with a large image of the logo on the back of the business card, and the business card details plus a design on the front.

Target Market(s)

High income earners in an affluent Melbourne suburb who value high quality products and done mind paying for it

Industry/Entity Type

Retail

Contact Information for Business Card

Business name: Haddleby's Fine Food Merchant
Address: 27 Quillmont Rd, Tarnvale VIC 3188
Name: TBC
Position Title: Director
Phone Number: TBC
Mobile: TBC

Business name is: Haddleby's Fine Food Merchant. Please allow space for us to fill in the business address, contact number, person's name, position Title and mobile number.

Colors
acd036

Requirements
Must have
• The logo must have our business logo on the back, and our business details and contact details on the front. It must include the colours of white, black and lime green
Nice to have
• It can have different background colours on the front and on the back.
Should not have
• It should not have any other colours aside from white, black and lime green

```html
<!DOCTYPE html>
<html lang="en">
<head>
<meta charset="UTF-8">
<title>Haddleby's Fine Food Merchant – Business Card</title>
<link rel="stylesheet" href="https://fonts.googleapis.com/css2?family=Zilla+Slab:wght@400;500;700&display=swap">
<style>
  :root {
    --ink: #111111;
    --paper: #ffffff;
    --lime: #acd036;
    --lime-soft: #e4f1bd;
    --backdrop: #ecebe7;
    --card-shadow: rgba(0, 0, 0, 0.18);
  }
  * { box-sizing: border-box; margin: 0; padding: 0; }
  html, body {
    width: 1200px;
    height: 800px;
    overflow: hidden;
    background: var(--backdrop);
    font-family: "Zilla Slab", Georgia, serif;
    color: var(--ink);
  }
  .canvas {
    position: relative;
    width: 1200px;
    height: 800px;
  }
  .card {
    position: absolute;
    top: 252px;
    width: 520px;
    height: 297px;
    border-radius: 3px;
    box-shadow: 0 10px 28px var(--card-shadow);
    overflow: hidden;
  }

  /* Back side */
  .card--back {
    left: 50px;
    background: var(--ink);
  }
  .brand-seal {
    position: absolute;
    left: 50%;
    top: 50%;
    width: 196px;
    height: 196px;
    margin: -98px 0 0 -98px;
    border-radius: 50%;
    background: var(--paper);
    display: flex;
    align-items: center;
    justify-content: center;
  }
  .brand-seal__name {
    font-size: 27px;
    font-weight: 500;
    letter-spacing: 2px;
    text-transform: uppercase;
    color: var(--ink);
  }

  /* Front side */
  .card--front {
    left: 630px;
    background: var(--paper);
  }
  .holder {
    position: absolute;
    left: 40px;
    top: 46px;
  }
  .holder__name {
    font-size: 23px;
    font-weight: 700;
    letter-spacing: 0.5px;
    line-height: 1;
  }
  .holder__title {
    font-size: 15px;
    font-weight: 400;
    margin-top: 3px;
  }
  .divider {
    position: absolute;
    left: 0;
    top: 122px;
    width: 386px;
    height: 1.5px;
    background: var(--ink);
  }
  .produce-art {
    position: absolute;
    left: 384px;
    top: 60px;
    width: 110px;
    height: 140px;
    border-radius: 48% 48% 40% 40%;
    background: linear-gradient(160deg, var(--lime) 0%, var(--lime-soft) 45%, var(--paper) 100%);
  }
  .contact-lines {
    position: absolute;
    left: 40px;
    top: 176px;
    list-style: none;
    font-size: 14px;
    line-height: 21px;
  }
  .contact-lines li {
    display: flex;
    align-items: center;
    gap: 7px;
  }
  .contact-lines svg { width: 11px; height: 13px; }
  .business {
    position: absolute;
    right: 42px;
    bottom: 30px;
    text-align: right;
    font-size: 14px;
    line-height: 20px;
  }
  .business__name { font-weight: 700; }
  .business__address { font-weight: 400; }
</style>
</head>
<body>
<main class="canvas">
  <section class="card card--back" aria-label="Business card back">
    <div class="brand-seal">
      <span class="brand-seal__name">Haddleby's</span>
    </div>
  </section>

  <section class="card card--front" aria-label="Business card front">
    <div class="holder">
      <p class="holder__name">LOREM IPSUM</p>
      <p class="holder__title">Director</p>
    </div>
    <div class="divider"></div>
    <div class="produce-art" role="img" aria-label="Line illustration of a jar, beetroot and apple with lime green leaves"></div>
    <ul class="contact-lines">
      <li>
        <svg viewBox="0 0 11 13" aria-hidden="true"><path d="M2.5 1 L4.5 3.5 L3.4 5 Q4.6 7.8 6.6 9 L8 8 L10.5 10 L9 12 Q3 11 1 3 Z" fill="var(--ink)"/></svg>
        012 345 6789
      </li>
      <li>
        <svg viewBox="0 0 11 13" aria-hidden="true"><rect x="2" y="0.8" width="7" height="11.4" rx="1" fill="none" stroke="var(--ink)" stroke-width="1.3"/><line x1="4.5" y1="10.4" x2="6.5" y2="10.4" stroke="var(--ink)" stroke-width="1"/></svg>
        012 345 6789
      </li>
    </ul>
    <div class="business">
      <p class="business__name">Haddleby's Fine Food Merchant</p>
      <p class="business__address">27 Quillmont Rd, Tarnvale VIC 3188</p>
    </div>
  </section>
</main>
</body>
</html>
```